Maple Hollow Bloom Panels Business card

Looking to have a business card design incorporating my logo for my flower wall business.

Industry/Entity Type

Wedding & event planning

Contact Information for Business Card

My business logo, my name - Lena Whitcombe (owner), my tagline - Let us be your something extra, phone # 401-726-3148, email address - maplehollowbloompanels@mailvane.net, my website - maplehollowbloompanels.net, Instagram handle- @maplehollowbloompanels, FB handle Handle - maplehollowbloompanels

Font styles to use
Other font styles liked:
• Sentaina is the font that is used in my logo

Requirements
Must have
• Would like a double sided business card

```html
<!DOCTYPE html>
<html lang="en">
<head>
<meta charset="utf-8">
<title>Maple Hollow Bloom Panels – Business Card</title>
<link rel="stylesheet" href="https://fonts.googleapis.com/css2?family=Roboto+Condensed:wght@300;400&family=Allura&display=swap">
<style>
  :root {
    --backdrop: #e6e7e9;
    --card-white: #ffffff;
    --blush: #f9dee7;
    --blush-border: #f6d3df;
    --rose: #e38fc0;
    --ink: #333333;
    --rule: #3a3a3a;
    --gold: #d9b45a;
  }
  * { margin: 0; padding: 0; box-sizing: border-box; }
  html, body {
    width: 1067px; height: 1200px; overflow: hidden;
    background: var(--backdrop);
  }
  .canvas { position: relative; width: 1067px; height: 1200px; }

  .card { position: absolute; left: 98px; width: 877px; height: 501px; }
  .card-front {
    top: 61px; background: var(--card-white);
    border: 3px solid var(--blush-border);
  }
  .card-back { top: 620px; background: var(--blush); }

  .signature {
    position: absolute; left: 112px; top: 214px; width: 208px; text-align: right;
    font-family: "Allura", cursive; color: var(--rose);
  }
  .signature-name { display: block; font-size: 40px; line-height: 44px; white-space: nowrap; }
  .signature-role { display: block; font-size: 22px; line-height: 22px; color: #555; }

  .divider {
    position: absolute; left: 337px; top: 210px; width: 2px; height: 79px;
    background: var(--rose);
  }

  .contact-list { position: absolute; left: 362px; top: 200px; list-style: none; }
  .contact-item {
    display: flex; align-items: center; height: 34px;
    font-family: "Roboto Condensed", sans-serif; font-weight: 400;
    font-size: 25px; color: var(--ink);
  }
  .contact-icon { width: 22px; height: 22px; margin-right: 10px; flex: none; }

  .footer-rule {
    position: absolute; left: -5px; top: 427px; width: 868px; height: 2px;
    background: var(--rule);
  }
  .social {
    position: absolute; top: 445px; display: flex; align-items: center;
    font-family: "Roboto Condensed", sans-serif; font-size: 25px; color: var(--ink);
  }
  .social-facebook { left: 53px; }
  .social-instagram { left: 524px; }
  .social-square { width: 18px; height: 18px; background: var(--rose); margin-right: 17px; }
  .social-circle { width: 20px; height: 20px; border-radius: 50%; background: var(--rose); margin-right: 16px; }

  .brand-badge {
    position: absolute; left: 281px; top: 70px; width: 314px; height: 314px;
    border-radius: 50%; background: var(--card-white);
    display: flex; align-items: center; justify-content: center; text-align: center;
  }
  .brand-name {
    font-family: "Roboto Condensed", sans-serif; font-weight: 300;
    font-size: 34px; line-height: 40px; letter-spacing: 2px; color: var(--ink);
    text-transform: uppercase; width: 240px;
  }
  .tagline {
    position: absolute; left: 0; top: 408px; width: 100%; text-align: center;
    font-family: "Allura", cursive; font-size: 44px; color: var(--ink);
  }
</style>
</head>
<body>
<main class="canvas">
  <section class="card card-front" aria-label="Business card front">
    <div class="signature">
      <span class="signature-name">Lena Whitcombe</span>
      <span class="signature-role">owner</span>
    </div>
    <div class="divider"></div>
    <ul class="contact-list">
      <li class="contact-item">
        <svg class="contact-icon" viewBox="0 0 24 24" aria-hidden="true"><path fill="var(--rose)" d="M6.6 10.8a15 15 0 0 0 6.6 6.6l2.2-2.2c.3-.3.7-.4 1-.2 1.1.4 2.3.6 3.6.6.6 0 1 .4 1 1V20c0 .6-.4 1-1 1A17 17 0 0 1 3 4c0-.6.4-1 1-1h3.5c.6 0 1 .4 1 1 0 1.3.2 2.5.6 3.6.1.3 0 .7-.2 1z"/></svg>
        401-726-3148
      </li>
      <li class="contact-item">
        <svg class="contact-icon" viewBox="0 0 24 24" aria-hidden="true"><rect x="2" y="5" width="20" height="14" fill="var(--rose)"/><path d="M2 5l10 8 10-8" fill="none" stroke="#fff" stroke-width="1.5"/></svg>
        maplehollowbloompanels@mailvane.net
      </li>
      <li class="contact-item">
        <svg class="contact-icon" viewBox="0 0 24 24" aria-hidden="true"><circle cx="12" cy="12" r="10" fill="var(--rose)"/><ellipse cx="12" cy="12" rx="4" ry="10" fill="none" stroke="#fff" stroke-width="1.3"/><path d="M2 12h20" stroke="#fff" stroke-width="1.3"/></svg>
        maplehollowbloompanels.net
      </li>
    </ul>
    <div class="footer-rule"></div>
    <div class="social social-facebook"><span class="social-square"></span>maplehollowbloompanels</div>
    <div class="social social-instagram"><span class="social-circle"></span>@maplehollowbloompanels</div>
  </section>

  <section class="card card-back" aria-label="Business card back">
    <div class="brand-badge">
      <span class="brand-name">Maple Hollow Bloom Panels</span>
    </div>
    <p class="tagline">Let us be your something extra</p>
  </section>
</main>
</body>
</html>
```